Website Redesign for Mortgage, Property and Conveyancing business

Project Overview:
We are looking for a refresh and redesign of our current website to a smart, crisp and fresh approach to Home Loans, Conveyancing and Property sales. This task will be to:
- Redesign our current website in accordance with the new wireframe.
- Provide all elements required for the design
- Build 7 key templates including:
Home Page
2nd Level Section Page
3rd level Product landing Page
2nd Level - About Us, Contact Us etc
Blog
Blog Article
Campaign Page - no header
Technical
The design is for a Wordpress website. Existing theme is Quillnest and we use Elementor for page editing. We are open to a new theme to be introduced but would prefer to stay with elementor.
Current Site is: www.corvanta.com.au
Sites that we like or elements of sites:
Pelham Real Estate: https://www.pelham-example.com.au/ (Like use of video and navigation)
Copper Lantern Lane - Mortage: https://cll-example.com.au/refinance-home-loan/ (Like landing pages a sin example)
Marquetry: https://marquetry-example.com.au/ (like Our services section).
Industry/Entity Type
Mortgage, Property, Conveyancing, Property Investment
Coding
Coded - Design and coding required
Number of Pages Required
5+ page
Font styles to use
Requirements
Must have
- Built for Wordpress and Elementor.
Nice to have
- See Project Description for links to ideas/elements that we have liked. However, open to ideas as long as the follow the navigation set out in the wire frame.

```html
<!DOCTYPE html>
<html lang="en">
<head>
<meta charset="utf-8">
<title>Corvanta Group Services — Finance, Property, Conveyancing</title>
<link href="https://fonts.googleapis.com/css2?family=Poppins:wght@300;400;500;600;700&display=swap" rel="stylesheet">
<style>
:root{
  --ink:#1d1d1f;
  --muted:#3a3a3a;
  --soft:#8a8a8a;
  --navy:#0b4a77;
  --navy-dark:#0a3f66;
  --green:#1fa84f;
  --card-grey:#dde2ea;
  --card-green:#dcf0e3;
  --card-blue:#dbe9f4;
  --quote:#e6f4fd;
  --quote-active:#8fd0fb;
  --tile:#f5f5f5;
  --line:#c9c9c9;
  --white:#ffffff;
}
*{box-sizing:border-box;margin:0;padding:0}
html,body{width:1200px;height:4892px;overflow:hidden}
body{position:relative;background:var(--white);font-family:'Poppins',sans-serif;color:var(--ink)}
.abs{position:absolute}

/* header */
.brand{left:118px;top:60px;display:flex;align-items:center;gap:8px;font-size:17px;font-weight:500;color:var(--ink)}
.brand-mark{width:20px;height:20px;background:var(--navy)}
.nav{left:604px;top:62px;display:flex;gap:34px;font-size:11px;color:var(--muted)}
.nav .active{font-weight:600;color:var(--ink)}
.search{left:1080px;top:62px}

/* hero */
.hero-title{left:0;width:1200px;top:148px;text-align:center;font-size:52px;font-weight:700;letter-spacing:-.5px}
.hero-sub{left:0;width:1200px;top:210px;text-align:center;font-size:37px;font-weight:300;color:var(--muted)}
.hero-copy{left:120px;width:960px;top:282px;text-align:center;font-size:19.5px;line-height:27px;color:var(--muted)}
.btn-primary{left:416px;top:395px;width:154px;height:53px;border-radius:6px;background:var(--navy);color:var(--white);font-size:20px;display:flex;align-items:center;justify-content:center}
.btn-link{left:610px;top:395px;height:53px;display:flex;align-items:center;gap:16px;font-size:20px;color:var(--navy)}
.hero-photo{left:0;top:488px;width:1200px;height:416px;background:linear-gradient(100deg,#3b3f3d 0%,#c9cbc8 22%,#eceae6 45%,#b9b6ae 62%,#7a5a3e 78%,#2a2d33 100%)}

/* services */
.section-title{font-size:36px;font-weight:600;line-height:42px}
.services-title{left:0;width:1200px;top:1036px;text-align:center}
.services-copy{left:100px;width:1000px;top:1155px;text-align:center;font-size:19.5px;line-height:27px;color:var(--muted)}
.service-card{top:1307px;width:316px;height:224px;border-radius:14px;padding:22px 20px}
.service-card .icon{width:50px;height:50px;border-radius:50%;background:var(--white);margin-bottom:22px}
.service-card h3{font-size:20px;font-weight:500;margin-bottom:6px}
.service-card p{font-size:14.5px;line-height:21px;color:var(--muted)}
.c-finance{left:100px;background:var(--card-grey)}
.c-property{left:442px;background:var(--card-green)}
.c-convey{left:784px;background:var(--card-blue)}

/* why */
.why-title{left:100px;top:1665px}
.why-copy{left:612px;width:490px;top:1664px;font-size:19.5px;line-height:27px;color:var(--muted)}
.step{width:574px;height:160px;border:1.5px solid #9a9a9a;border-radius:10px;padding:24px 26px;background:var(--white)}
.step h3{font-size:26px;font-weight:400;line-height:36px;margin-bottom:12px;white-space:nowrap;letter-spacing:-.2px}
.step p{font-size:11.5px;line-height:20px;color:var(--soft);width:470px}
.s1{left:184px;top:1835px}.s2{left:441px;top:2022px}.s3{left:184px;top:2208px}.s4{left:441px;top:2394px}
.dash{width:0;border-left:2px dashed #9a9a9a}
.d1{left:329px;top:1997px;height:211px}
.d2{left:866px;top:2183px;height:211px}

/* testimonials */
.clients-title{left:100px;top:2688px}
.clients-copy{left:100px;width:640px;top:2754px;font-size:19.5px;line-height:27px;color:var(--muted)}
.arrow-prev{left:930px;top:2743px}
.arrow-next{left:990px;top:2736px;width:50px;height:50px;border-radius:50%;background:var(--navy);display:flex;align-items:center;justify-content:center}
.rule{left:100px;width:1000px;height:2px;background:var(--line)}
.quote{top:2880px;width:232px;height:316px;background:var(--quote);padding:20px 20px}
.quote h4{font-size:16px;font-weight:500;line-height:23px;margin-bottom:14px}
.quote p{font-size:12.5px;line-height:20px;color:var(--muted)}
.quote .who{position:absolute;left:20px;bottom:16px;font-size:16px;line-height:22px}
.quote.active{background:var(--quote-active)}
.q1{left:100px}.q2{left:355px}.q3{left:612px}.q4{left:868px}
.divider{top:2880px;width:2px;height:316px;background:#bdbdbd}

/* listings */
.sales-title{left:100px;top:3338px}
.sales-copy{left:526px;width:560px;top:3340px;font-size:19.5px;line-height:27px;color:var(--muted)}
.listing{width:487px;height:377px;background:var(--tile);border-radius:14px;padding:16px}
.listing .photo{width:455px;height:246px;border-radius:14px}
.listing h4{font-size:15px;font-weight:600;margin:20px 0 6px}
.listing p{font-size:12.5px;line-height:19px;color:var(--soft)}
.lounge{background:linear-gradient(100deg,#6e6e6c 0%,#b7b3aa 30%,#3b4b3e 55%,#d9d7d2 80%,#a6a39c 100%)}
.kitchen{background:linear-gradient(180deg,#f1f1ef 0%,#e4e3df 55%,#b58a5a 80%,#cfcbc3 100%)}

/* footer */
.footer{left:0;top:4375px;width:1200px;height:517px;background:var(--navy)}
.cta-title{left:0;width:1200px;top:4492px;text-align:center;font-size:33px;font-weight:600;line-height:46px;color:var(--white)}
.cta-btn{left:479px;top:4649px;width:243px;height:71px;border-radius:36px;background:var(--green);color:var(--white);font-size:26px;font-weight:600;display:flex;align-items:center;justify-content:center;gap:16px}
.cta-btn .dot{width:40px;height:40px;border-radius:50%;background:var(--white);display:flex;align-items:center;justify-content:center}
.foot-brand{left:100px;top:4795px;width:134px;height:40px;background:var(--white);display:flex;align-items:center;justify-content:center;gap:6px;font-size:15px;font-weight:500;color:var(--ink)}
.foot-brand span.sq{width:14px;height:14px;background:var(--navy)}
.foot-nav{left:416px;top:4804px;display:flex;gap:16px;font-size:16px;color:var(--white)}
.socials{left:982px;top:4806px;display:flex;gap:8px}
.socials span{width:16px;height:16px;border-radius:50%;background:var(--white)}
</style>
</head>
<body>

<header>
  <div class="abs brand"><span class="brand-mark"></span>Corvanta</div>
  <nav class="abs nav">
    <span class="active">Home</span><span>About</span><span>Our Service</span><span>Gallery</span><span>More</span><span>Contact Us</span>
  </nav>
  <svg class="abs search" width="22" height="22" viewBox="0 0 22 22" fill="none" stroke="#0b4a77" stroke-width="1.6"><circle cx="10" cy="10" r="7"/><path d="M15 15l4 4"/></svg>
</header>

<section class="hero">
  <h1 class="abs hero-title">Finance, Property, Conveyancing</h1>
  <p class="abs hero-sub">Unlocking Opportunities and solving problems.</p>
  <p class="abs hero-copy">We’ve been in business for over 20 years. Corvanta Group Services is the all-in-one answer to reaching your property and financial goals more easily.&nbsp; We work with you to develop options to fit your current situation and to achieve your future objectives.</p>
  <a class="abs btn-primary">See home</a>
  <a class="abs btn-link">Watch tour
    <svg width="42" height="14" viewBox="0 0 42 14" fill="none" stroke="#0b4a77" stroke-width="1.8"><path d="M0 7h40M33 1l7 6-7 6"/></svg>
  </a>
  <div class="abs hero-photo" role="img" aria-label="Bright open-plan living room with sofa, kitchen and timber feature wall"></div>
</section>

<section class="services">
  <h2 class="abs section-title services-title">What do you get when<br>use our service</h2>
  <p class="abs services-copy">Lorem ipsum dolor sit amet consectetur. Quam lacus aliquet ligula ullamcorper mauris viverra velit eu posuere. Auctor eu metus urna in fermentum. Placerat diam auctor in interdum amet egestas ipsum vel. Nisl lorem egestas lacus est mauris mauris et nunc.</p>
  <div class="abs service-card c-finance"><div class="icon"></div><h3>Finance</h3><p>for your home, car, investments,<br>and assets</p></div>
  <div class="abs service-card c-property"><div class="icon"></div><h3>Property</h3><p>sales, purchases, and rentals</p></div>
  <div class="abs service-card c-convey"><div class="icon"></div><h3>Conveyancing</h3><p>for seamless property transactions</p></div>
</section>

<section class="why">
  <h2 class="abs section-title why-title">Why Choose Corvanta</h2>
  <p class="abs why-copy">Lorem ipsum dolor sit amet consectetur. Quam lacus aliquet ligula ullamcorper mauris viverra velit eu posuere. Auctor eu metus urna in fermentum.</p>
  <div class="abs dash d1"></div>
  <div class="abs dash d2"></div>
  <div class="abs step s1"><h3>20 years experience</h3><p>We have grown and changed with the industry, and we’re dedicated to continually improve our service and products so you get the best solutions possible.</p></div>
  <div class="abs step s2"><h3>We give you choice</h3><p>Working with over 20 large and small lenders, property developers and switched on accountants, we have the scope to give you good choices for the future.</p></div>
  <div class="abs step s3"><h3>It is about the outcome</h3><p>When we say we care, we mean it. If you are a client now, we want you to be a happy client. If we cannot help you become a client today we’d like to help you tomorrow.</p></div>
  <div class="abs step s4"><h3>We give you options that makes sense</h3><p>Our team of finance, property investment and accounting experts know what they are talking about, and they are happy to take the time to explain things clearly.</p></div>
</section>

<section class="clients">
  <h2 class="abs section-title clients-title">What Our Clients Say</h2>
  <p class="abs clients-copy">Lorem ipsum dolor sit amet consectetur. Quam lacus aliquet ligula ullamcorper mauris viverra velit eu posuere. Auctor eu metus urna in fermentum.</p>
  <svg class="abs arrow-prev" width="30" height="36" viewBox="0 0 30 36" fill="none" stroke="#0b4a77" stroke-width="2.2"><path d="M20 8L10 18l10 10"/></svg>
  <div class="abs arrow-next"><svg width="20" height="24" viewBox="0 0 20 24" fill="none" stroke="#fff" stroke-width="2.2"><path d="M6 4l8 8-8 8"/></svg></div>
  <div class="abs rule" style="top:2868px"></div>
  <div class="abs quote q1"><h4>Fantastic Team! Found My Dream Home!</h4><p>Lorem ipsum dolor sit amet consectetur. Quam lacus aliquet ligula ullamcorper mauris viverra velit eu posuere. Auctor eu metus urna in fermentum.</p><div class="who">Maren Holt<br>CEO</div></div>
  <div class="abs divider" style="left:341px"></div>
  <div class="abs quote q2"><h4>Fantastic Team! Found My Dream Home!</h4><p>Lorem ipsum dolor sit amet consectetur. Quam lacus aliquet ligula ullamcorper mauris viverra velit eu posuere. Auctor eu metus urna in fermentum.</p><div class="who">Maren Holt<br>CEO</div></div>
  <div class="abs divider" style="left:599px"></div>
  <div class="abs quote q3"><h4>Fantastic Team! Found My Dream Home!</h4><p>Lorem ipsum dolor sit amet consectetur. Quam lacus aliquet ligula ullamcorper mauris viverra velit eu posuere. Auctor eu metus urna in fermentum.</p><div class="who">Maren Holt<br>CEO</div></div>
  <div class="abs divider" style="left:855px"></div>
  <div class="abs quote q4 active"><h4>Fantastic Team! Found My Dream Home!</h4><p>Lorem ipsum dolor sit amet consectetur. Quam lacus aliquet ligula ullamcorper mauris viverra velit eu posuere. Auctor eu metus urna in fermentum.</p><div class="who">Maren Holt<br>CEO</div></div>
  <div class="abs rule" style="top:3202px"></div>
</section>

<section class="sales">
  <h2 class="abs section-title sales-title">New Object In Sales</h2>
  <p class="abs sales-copy">Lorem ipsum dolor sit amet consectetur. Quam lacus aliquet ligula ullamcorper mauris viverra velit eu posuere. Auctor eu metus urna in fermentum.</p>
  <article class="abs listing" style="left:100px;top:3469px"><div class="photo lounge" role="img" aria-label="Penthouse living room with grey sofa and large windows"></div><h4>Cozy Modern Penthouse</h4><p>Lorem ipsum dolor sit amet consectetur. Gravida leo ut semper urna.</p></article>
  <article class="abs listing" style="left:613px;top:3469px"><div class="photo kitchen" role="img" aria-label="White kitchen with island bench and timber stools"></div><h4>Clean Kitchen</h4><p>Lorem ipsum dolor sit amet consectetur. Gravida leo ut semper urna.</p></article>
  <article class="abs listing" style="left:100px;top:3868px"><div class="photo lounge" role="img" aria-label="Penthouse living room with grey sofa and large windows"></div><h4>Cozy Modern Penthouse</h4><p>Lorem ipsum dolor sit amet consectetur. Gravida leo ut semper urna.</p></article>
  <article class="abs listing" style="left:613px;top:3868px"><div class="photo kitchen" role="img" aria-label="White kitchen with island bench and timber stools"></div><h4>Clean Kitchen</h4><p>Lorem ipsum dolor sit amet consectetur. Gravida leo ut semper urna.</p></article>
</section>

<footer>
  <div class="abs footer"></div>
  <h2 class="abs cta-title">Need Property’s For<br>A Project</h2>
  <a class="abs cta-btn">Contact Us
    <span class="dot"><svg width="20" height="20" viewBox="0 0 24 24" fill="none" stroke="#0b4a77" stroke-width="1.8"><path d="M5 3h4l2 5-2.5 1.5a11 11 0 0 0 6 6L16 13l5 2v4a2 2 0 0 1-2 2A16 16 0 0 1 3 5a2 2 0 0 1 2-2z"/></svg></span>
  </a>
  <div class="abs foot-brand"><span class="sq"></span>Corvanta</div>
  <nav class="abs foot-nav"><span>Home</span><span>Service</span><span>Company</span><span>News</span><span>Contact</span></nav>
  <div class="abs socials"><span></span><span></span><span></span><span></span><span></span></div>
</footer>

</body>
</html>
```